Stationery Design Task - Stationary, memo and report templates for professional services company

Looking for someone to update stationary design but just as importantly come up with a template for reports and memos for use in our consulting firm. Would also like some brand use guidelines to be able to share with our whole team. We have an existing logo that we like. Need to update with a more contemporary look so that our deliverables to clients look good and professional yet stylish. This is for business to business communications. No need for envelope design. Important to have design for multiple pages, i.e. first page of a report and then 2nd page. Need to use in MS word documents so must be easy to use and replicate. Don't want something overly complex. Clean, fresh looking is best.

Industry/Entity Type

Information Technology

Font styles to use
Sans Serif

Colors
33a6d7
0792cd
85cae6
cee9f5
cedeed
85abd2
3377b5
0455a3

Requirements
Must have
• Clean look but with a little style or pop. Something that can easily be used in word documents. Need to have page styles that have a first page of a report (not a cover page) and then secondary page.
Nice to have
• - Although the dark blue is our primary color. Might be willing to look at some accent color as well.
Should not have
• Not just our logo on the page with a color bar.

```html
<!DOCTYPE html>
<html lang="en">
<head>
<meta charset="utf-8">
<title>Northvale Technology – Letterhead Set</title>
<link rel="stylesheet" href="https://fonts.googleapis.com/css2?family=Roboto:wght@400;700&family=Roboto+Condensed:wght@700&display=swap">
<style>
  :root {
    --bg: #d3d3d3;
    --paper: #fbfbfb;
    --blue-light: #33a6d7;
    --blue-mid: #0792cd;
    --blue-dark: #0455a3;
    --grey-text: #555555;
    --body-text: #2b2b2b;
  }
  * { box-sizing: border-box; margin: 0; padding: 0; }
  html, body { width: 1200px; height: 710px; overflow: hidden; }
  body {
    background: var(--bg);
    font-family: "Roboto", Arial, sans-serif;
    position: relative;
  }
  .sheet {
    position: absolute;
    top: 135px;
    width: 330px;
    height: 440px;
    background: var(--paper);
    box-shadow: 0 6px 18px rgba(0,0,0,0.12);
    overflow: hidden;
  }
  .sheet--letter { left: 45px; }
  .sheet--second { left: 435px; }
  .sheet--third  { left: 825px; }

  .sheet__header, .sheet__footer { position: absolute; left: 0; width: 100%; }
  .sheet__header { top: 0; height: 66px; }
  .sheet__footer { bottom: 0; height: 60px; }
  .sheet__header svg, .sheet__footer svg { display: block; width: 100%; height: 100%; }

  .brand {
    position: absolute; top: 18px; left: 12px;
    display: flex; align-items: center; gap: 6px;
    color: #fff;
    font-family: "Roboto Condensed", Arial, sans-serif;
    font-weight: 700;
  }
  .brand__dot { width: 18px; height: 18px; border-radius: 50%; background: #fff; opacity: 0.9; }
  .brand__name { font-size: 15px; line-height: 1; letter-spacing: 0.2px; }
  .brand__name span { display: block; font-size: 6.5px; letter-spacing: 2.8px; margin-top: 2px; }

  .contact {
    position: absolute; top: 26px; right: 10px;
    text-align: right;
    font-size: 5.2px; line-height: 1.6;
    color: var(--grey-text);
  }
  .contact strong { font-weight: 700; color: #444; }

  .letter-body {
    position: absolute; top: 92px; left: 34px; right: 30px;
    font-size: 6.6px; line-height: 1.42;
    color: var(--body-text);
  }
  .letter-body p + p { margin-top: 8px; }

  .web {
    position: absolute; bottom: 8px; right: 12px;
    color: #fff; font-size: 6px; font-weight: 700;
  }
</style>
</head>
<body>

<section class="sheet sheet--letter">
  <div class="sheet__header">
    <svg viewBox="0 0 330 66" preserveAspectRatio="none" aria-hidden="true">
      <defs>
        <linearGradient id="blueHead1" x1="0" y1="0" x2="1" y2="1">
          <stop offset="0" stop-color="#0455a3"/>
          <stop offset="1" stop-color="#33a6d7"/>
        </linearGradient>
        <linearGradient id="greyHead1" x1="0" y1="0" x2="0" y2="1">
          <stop offset="0" stop-color="#e9e9e9"/>
          <stop offset="1" stop-color="#b7b7b7"/>
        </linearGradient>
      </defs>
      <rect x="0" y="0" width="330" height="5" fill="#dcdcdc"/>
      <polygon points="125,5 330,5 330,54 140,54" fill="url(#greyHead1)"/>
      <polygon points="140,54 330,54 330,60 143,60" fill="#0792cd"/>
      <polygon points="0,5 122,5 146,62 0,62" fill="url(#blueHead1)"/>
    </svg>
    <div class="brand">
      <div class="brand__dot"></div>
      <div class="brand__name">NORTHVALE<span>TECHNOLOGY</span></div>
    </div>
    <div class="contact">
      <strong>1200 Harbor Crest Way, Suite 40, Lakeview, Oregon 97001</strong><br>
      555-014-2290 &nbsp;|&nbsp; hello@northvaletech.com &nbsp;|&nbsp; www.northvaletech.com
    </div>
  </div>

  <div class="letter-body">
    <p>Lorem Ipsum is simply placeholder text of the printing and typesetting trade. Lorem Ipsum has been the standard filler text for many centuries, ever since an unknown printer took a galley of type and scrambled it to make a type specimen book. It has survived not only five centuries, but also the leap into electronic typesetting, remaining essentially unchanged. It became widely known in the 1960s with the release of transfer sheets containing Lorem Ipsum passages, and more recently with desktop layout software that includes versions of Lorem Ipsum.</p>
    <p>It is a long established fact that a reader will be distracted by the readable content of a page when looking at its layout. The point of using Lorem Ipsum is that it has a more-or-less normal distribution of letters, as opposed to using 'Content here, content here', making it look like readable English. Many desktop publishing packages and web page editors now use Lorem Ipsum as their default model text, and a search for 'lorem ipsum' will uncover many web sites still in their infancy. Various versions have evolved over the years, sometimes by accident, sometimes on purpose (injected humour and the like).</p>
    <p>Contrary to popular belief, Lorem Ipsum is not simply random text. It has roots in a piece of classical Latin literature from 45 BC, making it over 2000 years old. A language teacher at a small regional college looked up one of the more obscure Latin words, consectetur, from a Lorem Ipsum passage, and going through the uses of the word in classical literature, discovered the undoubtable source. Lorem Ipsum comes from two short sections of an ancient treatise on ethics, reworked with model sentence structures to generate text which looks reasonable. The generated Lorem Ipsum is therefore always free from repetition, injected humour or non-characteristic words etc.</p>
  </div>

  <div class="sheet__footer">
    <svg viewBox="0 0 330 60" preserveAspectRatio="none" aria-hidden="true">
      <defs>
        <linearGradient id="blueFoot1" x1="0" y1="0" x2="1" y2="1">
          <stop offset="0" stop-color="#33a6d7"/>
          <stop offset="1" stop-color="#0455a3"/>
        </linearGradient>
      </defs>
      <rect x="0" y="6" width="330" height="3" fill="#33a6d7"/>
      <rect x="0" y="12" width="330" height="2" fill="#b9b9b9"/>
      <polygon points="0,18 330,18 330,36 200,36 190,24 0,24" fill="#e3e3e3"/>
      <polygon points="190,34 330,34 330,60 206,60" fill="url(#blueFoot1)"/>
    </svg>
  </div>
</section>

<section class="sheet sheet--second">
  <div class="sheet__header">
    <svg viewBox="0 0 330 66" preserveAspectRatio="none" aria-hidden="true">
      <defs>
        <linearGradient id="blueHead2" x1="0" y1="0" x2="1" y2="1">
          <stop offset="0" stop-color="#0455a3"/>
          <stop offset="1" stop-color="#33a6d7"/>
        </linearGradient>
        <linearGradient id="greyHead2" x1="0" y1="0" x2="0" y2="1">
          <stop offset="0" stop-color="#e9e9e9"/>
          <stop offset="1" stop-color="#b7b7b7"/>
        </linearGradient>
      </defs>
      <rect x="0" y="0" width="330" height="5" fill="#dcdcdc"/>
      <polygon points="125,5 330,5 330,54 140,54" fill="url(#greyHead2)"/>
      <polygon points="140,54 330,54 330,60 143,60" fill="#0792cd"/>
      <polygon points="0,5 122,5 146,62 0,62" fill="url(#blueHead2)"/>
    </svg>
    <div class="brand">
      <div class="brand__dot"></div>
      <div class="brand__name">NORTHVALE<span>TECHNOLOGY</span></div>
    </div>
  </div>
  <div class="sheet__footer">
    <svg viewBox="0 0 330 60" preserveAspectRatio="none" aria-hidden="true">
      <defs>
        <linearGradient id="blueFoot2" x1="0" y1="0" x2="1" y2="1">
          <stop offset="0" stop-color="#33a6d7"/>
          <stop offset="1" stop-color="#0455a3"/>
        </linearGradient>
      </defs>
      <rect x="0" y="6" width="330" height="3" fill="#33a6d7"/>
      <rect x="0" y="12" width="330" height="2" fill="#b9b9b9"/>
      <polygon points="0,18 330,18 330,36 200,36 190,24 0,24" fill="#e3e3e3"/>
      <polygon points="190,34 330,34 330,60 206,60" fill="url(#blueFoot2)"/>
    </svg>
    <div class="web">www.northvaletech.com</div>
  </div>
</section>

<section class="sheet sheet--third">
  <div class="sheet__header">
    <svg viewBox="0 0 330 66" preserveAspectRatio="none" aria-hidden="true">
      <defs>
        <linearGradient id="blueHead3" x1="0" y1="0" x2="1" y2="1">
          <stop offset="0" stop-color="#0455a3"/>
          <stop offset="1" stop-color="#33a6d7"/>
        </linearGradient>
        <linearGradient id="greyHead3" x1="0" y1="0" x2="0" y2="1">
          <stop offset="0" stop-color="#e9e9e9"/>
          <stop offset="1" stop-color="#b7b7b7"/>
        </linearGradient>
      </defs>
      <rect x="0" y="0" width="330" height="5" fill="#dcdcdc"/>
      <polygon points="125,5 330,5 330,54 140,54" fill="url(#greyHead3)"/>
      <polygon points="140,54 330,54 330,60 143,60" fill="#0792cd"/>
      <polygon points="0,5 122,5 146,62 0,62" fill="url(#blueHead3)"/>
    </svg>
    <div class="brand">
      <div class="brand__dot"></div>
      <div class="brand__name">NORTHVALE<span>TECHNOLOGY</span></div>
    </div>
  </div>
  <div class="sheet__footer">
    <svg viewBox="0 0 330 60" preserveAspectRatio="none" aria-hidden="true">
      <defs>
        <linearGradient id="blueFoot3" x1="0" y1="0" x2="1" y2="1">
          <stop offset="0" stop-color="#33a6d7"/>
          <stop offset="1" stop-color="#0455a3"/>
        </linearGradient>
      </defs>
      <rect x="0" y="6" width="330" height="3" fill="#33a6d7"/>
      <rect x="0" y="12" width="330" height="2" fill="#b9b9b9"/>
      <polygon points="0,18 330,18 330,36 200,36 190,24 0,24" fill="#e3e3e3"/>
      <polygon points="190,34 330,34 330,60 206,60" fill="url(#blueFoot3)"/>
    </svg>
    <div class="web">www.northvaletech.com</div>
  </div>
</section>

</body>
</html>
```